I need to redesign this website. Modern Fun Professional Redesign For www.JollyPerkHub.com = New Name www.ClaimVouchly.com

Use existing content as it is on website exactly and we will revise after initial mock ups.

The new name will be ClaimVouchly.com please make a quick logo for this site too while redesigning.

Make it look like an official website....

Target Market(s)

Consumers that are redeeming certificates that businesses gave to them as a gift for customer loyalty,e tc.

Industry/Entity Type

It Professional

Logo Text

www.ClaimVouchly.com

Number of Pages Required

4 page

Colors

Designer to choose colors to be used in the design.

Requirements
Must have
• Must look professional, build trust and credibility.
Nice to have
• open
Should not have
• open

```html
<!DOCTYPE html>
<html lang="en">
<head>
<meta charset="utf-8">
<title>ClaimVouchly – Redemption Processing Center</title>
<link href="https://fonts.googleapis.com/css2?family=Lato:ital,wght@0,400;0,700;1,400&family=PT+Sans:wght@400;700&display=swap" rel="stylesheet">
<style>
:root{
  --blue:#1c8fd2;
  --orange:#f47b20;
  --green:#4a9a3a;
  --ink:#333333;
  --hero-light:#f3f3f3;
  --hero-dark:#cdcdcd;
  --band:#ececec;
  --card-border:#d9d9d9;
  --quote-bg:#707070;
  --footer:#333333;
}
*{margin:0;padding:0;box-sizing:border-box}
html,body{width:1098px;height:1200px;overflow:hidden;background:#fff}
body{position:relative;font-family:"Lato",sans-serif;color:var(--ink)}
.abs{position:absolute}

/* header */
.site-header{position:absolute;left:0;top:0;width:1098px;height:103px;background:#fff}
.brand-mark{left:74px;top:14px;width:72px;height:72px;border-radius:50%;background:var(--blue)}
.brand-name{left:165px;top:18px;font-family:"PT Sans",sans-serif;font-weight:700;font-size:32px;line-height:1.2;color:var(--blue)}
.brand-tag{left:165px;top:57px;font-family:"PT Sans",sans-serif;font-size:16px;color:var(--ink)}
.phone{right:76px;top:13px;display:flex;align-items:center;gap:7px;font-size:15px;color:var(--ink)}
.phone-icon{width:29px;height:29px;border-radius:50%;background:var(--green);display:flex;align-items:center;justify-content:center}
.main-nav{right:76px;top:62px;display:flex;align-items:center;font-size:14px}
.main-nav a{color:var(--ink);text-decoration:none;padding:0 25px;border-left:1px solid #ccc;line-height:12px}
.main-nav a:first-child{border-left:none}
.main-nav a:last-child{padding-right:0}
.main-nav a.active{color:var(--blue)}

/* hero */
.hero{position:absolute;left:0;top:103px;width:1098px;height:450px;
  background:radial-gradient(ellipse at 60% 20%,var(--hero-light) 0%,#e2e2e2 50%,var(--hero-dark) 100%)}
.hero-title{position:absolute;left:0;width:100%;top:110px;text-align:center;font-family:"PT Sans",sans-serif;font-weight:400;font-size:37px;line-height:1.2;color:var(--blue)}
.hero-title span{color:var(--orange)}
.hero-line{position:absolute;left:0;width:100%;text-align:center;font-size:20.5px;color:var(--ink);text-transform:uppercase}
.redeem-form{position:absolute;left:129px;top:260px;width:840px;height:70px;background:#f3f3f3;padding:6px 7px}
.redeem-input{width:712px;height:58px;background:#fff;border:1px solid #e0e0e0;float:left}
.redeem-go{float:left;width:114px;height:58px;background:var(--green);color:#fff;font-family:"PT Sans",sans-serif;font-size:28px;display:flex;align-items:center;justify-content:center}

/* intro */
.intro{position:absolute;left:0;top:553px;width:1098px;height:155px;text-align:center;font-size:14px;color:var(--ink)}
.intro p{position:absolute;left:0;width:100%}

/* testimonials */
.testimonials{position:absolute;left:0;top:708px;width:1098px;height:447px;background:var(--band)}
.section-title{position:absolute;left:0;width:100%;top:32px;text-align:center;font-family:"PT Sans",sans-serif;font-weight:400;font-size:29px;line-height:1.2;color:var(--blue)}
.section-title span{color:var(--orange)}
.section-rule{position:absolute;left:529px;top:82px;width:40px;height:1px;background:#c4c4c4}
.card{position:absolute;top:157px;width:300px;height:213px;background:#fff;border:1px solid var(--card-border);text-align:center}
.quote-ring{position:absolute;left:97px;top:-52px;width:106px;height:106px;border-radius:50%;background:#e4e4e4;clip-path:inset(50% 0 0 0)}
.quote-badge{position:absolute;left:103px;top:-47px;width:93px;height:93px;border-radius:50%;background:var(--quote-bg);display:flex;align-items:center;justify-content:center}
.card-name{position:absolute;left:0;width:100%;top:67px;font-family:"PT Sans",sans-serif;font-size:16px;color:var(--blue)}
.card-stars{position:absolute;left:0;width:100%;top:90px;font-size:12px;letter-spacing:3px;color:var(--orange)}
.card-text{position:absolute;left:8px;right:8px;top:111px;font-size:12.2px;line-height:22px;color:var(--ink)}
.view-all{position:absolute;left:0;width:100%;top:390px;text-align:center;font-style:italic;font-size:15px}
.view-all a{color:var(--green);text-decoration:underline}

/* footer */
.site-footer{position:absolute;left:0;top:1155px;width:1098px;height:45px;background:var(--footer);color:#fff;font-size:14px}
.copyright{left:75px;top:13px}
.social{position:absolute;top:8px;width:29px;height:29px;border-radius:50%}
</style>
</head>
<body>

<header class="site-header">
  <div class="abs brand-mark"></div>
  <div class="abs brand-name">ClaimVouchly</div>
  <div class="abs brand-tag">Redemption Processing Center</div>
  <div class="abs phone">
    <span class="phone-icon">
      <svg width="15" height="15" viewBox="0 0 24 24"><path fill="#fff" d="M6.6 10.8c1.4 2.8 3.8 5.1 6.6 6.6l2.2-2.2c.3-.3.7-.4 1-.2 1.1.4 2.3.6 3.6.6.6 0 1 .4 1 1V20c0 .6-.4 1-1 1C10.6 21 3 13.4 3 4c0-.6.4-1 1-1h3.5c.6 0 1 .4 1 1 0 1.3.2 2.5.6 3.6.1.3 0 .7-.2 1L6.6 10.8z"/></svg>
    </span>
    555-014-2290
  </div>
  <nav class="abs main-nav">
    <a class="active" href="#">Home</a>
    <a href="#">Testimonials</a>
    <a href="#">Terms</a>
    <a href="#">Contact Us</a>
  </nav>
</header>

<section class="hero" role="img" aria-label="Soft grey faceted geometric backdrop">
  <h1 class="hero-title">Welcome To ClaimVouchly</h1>
  <p class="hero-line" style="top:171px">Please enter a valid certificate ID in the form below</p>
  <p class="hero-line" style="top:211px">To redeem your certificate and to view FAQ's, terms and locations.</p>
  <div class="redeem-form">
    <div class="redeem-input"></div>
    <div class="redeem-go">Go</div>
  </div>
</section>

<section class="intro">
  <p style="top:28px">ClaimVouchly.com is a leading company in travel certificate fulfillment.</p>
  <p style="top:52px">Our goal is to make it easy for you to redeem your certificate and our philosophy is this:</p>
  <p style="top:73px"><strong>"What good is it to receive a gift certificate if you can't use it?"</strong>.</p>
  <p style="top:98px">If you have any questions about how to redeem a certain certificate, please contact us. We are here to help.</p>
</section>

<section class="testimonials">
  <h2 class="section-title">Client <span>Testimonials</span></h2>
  <div class="section-rule"></div>

  <article class="card" style="left:73px">
    <div class="quote-ring"></div>
    <div class="quote-badge"><svg width="32" height="26" viewBox="0 0 32 26"><path fill="#fff" d="M2 0h11v11c0 8-4 13-11 15l-1-4c4-1 6-4 6-7H2zM19 0h11v11c0 8-4 13-11 15l-1-4c4-1 6-4 6-7h-5z"/></svg></div>
    <div class="card-name">Nora T.</div>
    <div class="card-stars">★★★★★</div>
    <p class="card-text">Wren was a "saving grace.' She followed up and helped me book the vacation and air fare. Wren was positive and did everything she promised to do.</p>
  </article>

  <article class="card" style="left:399px">
    <div class="quote-ring"></div>
    <div class="quote-badge"><svg width="32" height="26" viewBox="0 0 32 26"><path fill="#fff" d="M2 0h11v11c0 8-4 13-11 15l-1-4c4-1 6-4 6-7H2zM19 0h11v11c0 8-4 13-11 15l-1-4c4-1 6-4 6-7h-5z"/></svg></div>
    <div class="card-name">Owen Price</div>
    <div class="card-stars">★★★★★</div>
    <p class="card-text">Julian was able to put together our flight schedule. He was very patient with us and diligent in working out all the changes I was requesting. Thank you, Jules.</p>
  </article>

  <article class="card" style="left:724px">
    <div class="quote-ring"></div>
    <div class="quote-badge"><svg width="32" height="26" viewBox="0 0 32 26"><path fill="#fff" d="M2 0h11v11c0 8-4 13-11 15l-1-4c4-1 6-4 6-7H2zM19 0h11v11c0 8-4 13-11 15l-1-4c4-1 6-4 6-7h-5z"/></svg></div>
    <div class="card-name">Liam Hartley</div>
    <div class="card-stars">★★★★★</div>
    <p class="card-text">Our vacation was great!!!! We stayed at the Marisol Grand. We had a lot of fun. We do not have any pictures as everyone else took them. We celebrated our grandson's 21st birthday.</p>
  </article>

  <div class="view-all"><a href="#">View All +</a></div>
</section>

<footer class="site-footer">
  <div class="abs copyright">Copyright © 2017 ClaimVouchly. All Rights Reserved.</div>
  <span class="social" style="left:882px;background:#1d4fa0" aria-label="Social link"></span>
  <span class="social" style="left:920px;background:#10c3d6" aria-label="Social link"></span>
  <span class="social" style="left:958px;background:#1b87c9" aria-label="Social link"></span>
  <span class="social" style="left:995px;background:#e8401c" aria-label="Social link"></span>
</footer>

</body>
</html>
```